Relaunch Instagram Posts Design

We want to give you a better understanding about the expected outcome of this task, and give you a little bit of a background that should help you throughout.
We already have social media accounts, they aren’t active and the posts are outdated. We just finished our rebranding exercise, and accordingly we are planning to have a re-launch where we communicate our new identity, and rebuild our online existence, to enhance our social media presence and engagement.
Thus, we want to formulate the style of posting from the beginning, so that it reflects the identity overall and we can move forward with in a consistent manner.

Find attached details. We will share other files later. You need to read the attachment in the project to understand the requirement. Also, you should use the attached images in the project. You should also use products images from our website...www.bloomvantra.com
Our Primary color is #5725A9, PURPLE (based on color HEX Code)
Our Secondary colors #7C50BE, #A17BD3, #C5A6E8, #EAD1FD
Also, this secondary colors can be used #2B9348, #55A630, #80B918, #AACC00

Target Market(s)

Gift-givers who would like to bring a gift of value and meaning, representing the occasion

Industry/Entity Type

Flowers

Colors

Designer to choose colors to be used in the design.

Requirements
Must have
• Image based posts with little graphics + typography-based posts.... hammer on the emotional aspect, focusing on special moments such as using images related nice moments
Nice to have
• A full overview as in the brief (with all 21 posts), to give the sense of the design direction for us to know if it fits our new brand vision or not.
Should not have
• A typical commercial design direction that focuses so much on direct product communication. This definitely will be there, but we want this to be integrated with the other aspects.

```html
<!DOCTYPE html>
<html lang="en">
<head>
<meta charset="utf-8">
<title>Bloomvantra – Relaunch Instagram Grid</title>
<link rel="stylesheet" href="https://fonts.googleapis.com/css2?family=Great+Vibes&family=Pinyon+Script&family=Kaushan+Script&family=Poppins:wght@300;400;500;600&family=Oswald:wght@500&family=Cairo:wght@500&display=swap">
<style>
:root{
  --purple:#5725A9;
  --purple-2:#7C50BE;
  --purple-3:#A17BD3;
  --purple-4:#C5A6E8;
  --purple-5:#EAD1FD;
  --pink:#F6C6D6;
  --white:#FFFFFF;
  --grey:#E6E4E8;
  --gold:#B89A5E;
  --brown:#8A6A3A;
  --rose:#B3121A;
  --ink:#3B2A55;
}
*{margin:0;padding:0;box-sizing:border-box}
html,body{width:1200px;height:2711px;overflow:hidden;background:var(--white)}
body{font-family:"Poppins",sans-serif;color:var(--purple)}
.grid{display:grid;grid-template-columns:repeat(3,400px);grid-template-rows:repeat(5,387px) 776px;width:1200px;height:2711px}
.post{position:relative;overflow:hidden;border:1px solid #f0eef3}
.abs{position:absolute}
.photo{position:absolute}
.script{font-family:"Great Vibes",cursive;font-weight:400}
.pinyon{font-family:"Pinyon Script",cursive}
.brush{font-family:"Kaushan Script",cursive}
.brand{position:absolute;display:flex;align-items:center;gap:6px;font-family:"Poppins",sans-serif;font-weight:500;letter-spacing:1px;color:var(--purple);font-size:11px;text-transform:uppercase}
.brand .dot{width:10px;height:10px;border-radius:50%;background:var(--purple)}
.brand.light{color:var(--white)}
.brand.light .dot{background:var(--white)}

/* 1 */
.p-tend{background:var(--white)}
.p-tend .photo{left:0;top:0;width:242px;height:100%;background:linear-gradient(160deg,#6b6b6b,#d8d6d2 40%,#a9a9a6 70%,#4d4b4a)}
.p-tend .frame{left:18px;top:18px;right:18px;bottom:26px;border:1px solid rgba(255,255,255,.9)}
.p-tend .lead{left:116px;top:58px;font-size:12px;color:var(--white)}
.p-tend .word{left:162px;top:66px;font-size:108px;color:var(--purple-3);line-height:1}
.p-tend .body{left:241px;top:204px;font-size:11px;line-height:15px;color:var(--purple-3)}

/* 2 */
.p-promo{background:linear-gradient(120deg,#F7D2DD,#E6B8E0 45%,#A985E0)}
.p-promo .title{right:34px;top:26px;font-size:50px;line-height:52px;color:var(--white);text-align:right}
.p-promo .arch-line{left:22px;top:130px;width:230px;height:240px;border:2px solid rgba(255,255,255,.8);border-radius:115px 115px 0 0}
.p-promo .photo{left:34px;top:142px;width:206px;height:228px;border-radius:103px 103px 0 0;background:linear-gradient(180deg,#e9ecef,#f4d7e0 35%,#d98aa2 55%,#cfcfcf 80%,#eeeeee)}
.p-promo .off{left:270px;top:186px;font-family:"Playfair Display",serif;color:var(--white);text-align:center}
.p-promo .off b{font-size:50px;font-weight:400}
.p-promo .off span{font-size:28px}
.p-promo .off i{display:block;font-style:normal;font-size:28px;letter-spacing:2px;margin-top:-6px}

/* 3 */
.p-orchid .photo{inset:0;background:linear-gradient(170deg,#e6a2c4,#d46e9d 35%,#f1d6dc 60%,#d8d4d0)}
.p-orchid .corner{width:40px;height:40px;border-color:var(--white);border-style:solid}
.p-orchid .lead{left:0;right:0;top:152px;text-align:center;font-size:10px;color:var(--white)}
.p-orchid .word{left:36px;top:160px;font-size:46px;color:var(--white)}
.p-orchid .tail{right:30px;top:206px;font-size:10px;color:var(--white)}

/* 4 */
.p-moment{background:linear-gradient(100deg,#D9CBEE,#B99BE6 55%,#8E63D2)}
.p-moment .card{left:22px;top:4px;width:262px;height:356px;background:var(--white);box-shadow:0 2px 10px rgba(0,0,0,.15)}
.p-moment .photo{left:30px;top:12px;width:246px;height:340px;background:linear-gradient(180deg,#f3f1ee,#ece6e0 50%,#c0262e 75%,#efeae4)}
.p-moment .quote{right:112px;top:24px;text-align:right;font-size:10px;line-height:14px;color:var(--ink)}
.p-moment .word{left:108px;top:52px;font-size:84px;color:var(--purple)}
.p-moment .ghost{left:180px;top:120px;font-size:74px;color:rgba(255,255,255,.35)}

/* 5 */
.p-power{background:linear-gradient(135deg,#CDB6F1,#B48EE8 50%,#9D74DE)}
.p-power .diag{right:0;top:0;width:100%;height:100%;background:var(--white);clip-path:polygon(88% 0,100% 0,100% 100%,30% 100%,30% 88%)}
.p-power .photo{left:22px;top:26px;width:270px;height:318px;transform:rotate(-5deg);background:linear-gradient(180deg,#e9e9ea,#d8d8d8 40%,#b0121c 55%,#3b3b3b 75%,#d9c6a8);box-shadow:0 4px 14px rgba(0,0,0,.2)}
.p-power .text{left:130px;top:58px;font-size:28px;line-height:30px;color:var(--purple-2);transform:rotate(-5deg)}
.p-power .brand{right:16px;bottom:24px}

/* 6 */
.p-rose .photo{inset:0;background:radial-gradient(circle at 20% 20%,#e0212b,#a00d16 45%,#5a0207 100%)}
.p-rose .frame{left:62px;top:70px;width:280px;height:290px;border:1.5px solid var(--gold)}
.p-rose .card{left:62px;top:100px;width:280px;height:235px;background:#f2ece6}
.p-rose .obj{left:150px;top:170px;width:180px;height:150px;background:linear-gradient(180deg,#f4ede6,#d9b15a 45%,#b58a52 70%,#c9a37a)}
.p-rose .small{left:86px;top:112px;font-size:9.5px;line-height:13px;color:#6e5b43}
.p-rose .w{font-family:"Oswald",sans-serif;color:var(--brown);line-height:1}
.p-rose .beauty{left:142px;top:22px;font-size:58px}
.p-rose .hope{left:4px;top:330px;font-size:58px;transform:rotate(-90deg);transform-origin:0 0}
.p-rose .love{left:385px;top:178px;font-size:58px;transform:rotate(90deg);transform-origin:0 0}

/* 7 */
.p-each{background:linear-gradient(170deg,#FBE8EE,#F3C8D5 45%,#B99BE6 85%,#9C72DD)}
.p-each .arch{left:0;top:18px;width:228px;height:370px;background:var(--purple-4);border-radius:0 114px 0 0}
.p-each .photo{left:0;top:30px;width:208px;height:357px;border-radius:0 104px 0 0;background:linear-gradient(180deg,#e8e4de,#f3efe9 30%,#d9a4bb 55%,#a36c8b 75%,#d9d2c5)}
.p-each .text{left:248px;top:120px;font-size:13px;line-height:18px;color:var(--purple)}
.p-each .text .s{font-family:"Kaushan Script",cursive;font-size:24px;color:var(--purple)}

/* 8 */
.p-priceless .photo{inset:0;background:radial-gradient(circle at 60% 55%,#d51a25,#9a0b13 55%,#f1ece8 90%)}
.p-priceless .frame{left:22px;top:18px;right:18px;bottom:20px;border:1px solid rgba(255,255,255,.8)}
.p-priceless .brand{left:40px;top:38px}
.p-priceless .title{left:60px;top:200px;font-size:46px;color:var(--white)}
.p-priceless .sub{left:146px;top:258px;font-size:13px;color:var(--white)}

/* 9 */
.p-collect{background:var(--grey)}
.p-collect .white{right:0;top:0;width:110px;height:100%;background:var(--white)}
.p-collect .band{left:116px;top:42px;width:284px;height:160px;background:linear-gradient(120deg,#F1EAF8,#D7C2F1 50%,#B594E8)}
.p-collect .photo{left:56px;top:180px;width:228px;height:207px;background:radial-gradient(circle at 50% 40%,#a07bd6,#6f43b4 60%,#4b2a86)}
.p-collect .frame{left:92px;top:22px;width:278px;height:322px;border:1px solid var(--gold)}
.p-collect .title{left:64px;top:82px;font-size:52px;color:var(--purple)}
.p-collect .sub{left:222px;top:142px;font-size:17px;color:var(--ink)}

/* 10 */
.p-remember .photo{inset:0;background:linear-gradient(160deg,#d94fae,#f1d2e4 35%,#f6f1f4 60%,#c7a0d8 85%,#7d3ca5)}
.p-remember .l1{left:96px;top:50px;font-size:16px;color:var(--purple)}
.p-remember .l2{left:114px;top:68px;font-size:32px;color:var(--purple)}
.p-remember .l3{left:40px;top:96px;font-size:80px;color:var(--purple);line-height:1}
.p-remember .frame{left:128px;top:182px;width:196px;height:160px;border:1px solid rgba(255,255,255,.9)}

/* 11 */
.p-logo{background:var(--white);display:flex;align-items:center;justify-content:center}
.p-logo .brand{position:static;font-size:26px;gap:14px;letter-spacing:2px}
.p-logo .brand .dot{width:22px;height:22px}

/* 12 */
.p-memories{background:#cfcfcf}
.p-memories .card{left:30px;top:12px;width:360px;height:352px;background:var(--white)}
.p-memories .lav{left:30px;top:200px;width:80px;height:164px;background:var(--purple-5)}
.p-memories .photo{left:0;top:40px;width:286px;height:220px;background:linear-gradient(160deg,#f0eeee,#e6c9cf 40%,#d1b7c0 60%,#9d8aa3)}
.p-memories .band{left:290px;top:40px;width:70px;height:235px;background:var(--purple-2)}
.p-memories .word{left:325px;top:158px;font-size:50px;color:var(--white);transform:translate(-50%,-50%) rotate(-90deg);white-space:nowrap}
.p-memories .frame{left:44px;top:40px;width:316px;height:276px;border:1px solid var(--purple-4)}
.p-memories .cap{left:110px;top:290px;width:280px;text-align:center;font-size:14px;line-height:20px;color:var(--purple-3)}
.p-memories .cap b{font-weight:600;color:var(--purple-3)}

/* 13 */
.p-journey .photo{inset:0;background:linear-gradient(90deg,#e6dfd3,#d0c7b8 48%,#bcbcbc 52%,#e7e7e7 80%,#9a9a9a)}
.p-journey .half{left:0;bottom:0;width:388px;height:118px;background:var(--purple);border-radius:194px 194px 0 0}
.p-journey .text{left:0;width:388px;bottom:18px;text-align:center;font-size:20px;line-height:26px;font-weight:300;color:var(--white);letter-spacing:.5px}

/* 14 */
.p-frozen{background:var(--purple-5)}
.p-frozen .tear{left:230px;top:18px;width:170px;height:90px;background:var(--white);clip-path:polygon(0 30%,40% 0,100% 0,100% 100%,30% 80%)}
.p-frozen .shade{left:50px;top:56px;width:290px;height:290px;background:var(--purple-3)}
.p-frozen .photo{left:34px;top:30px;width:238px;height:290px;background:linear-gradient(180deg,#d9d9d9,#8d8d8d 35%,#4a4a4a 60%,#c9c9c9)}
.p-frozen .label{left:140px;top:298px;padding:4px 12px;border:1.5px solid var(--purple);background:var(--white);outline:3px solid var(--white);font-size:16px;color:var(--purple)}

/* 15 */
.p-quote .photo{inset:0;background:linear-gradient(160deg,#3a3a3a,#777 40%,#9b9b9b 60%,#505050)}
.p-quote .box{left:106px;top:60px;width:190px;height:146px;border:1.5px solid rgba(255,255,255,.85);border-radius:18px}
.p-quote .mark{font-family:"Playfair Display",serif;font-size:64px;color:var(--white);line-height:1}
.p-quote .m1{left:100px;top:28px}
.p-quote .m2{left:254px;top:164px}
.p-quote .text{left:112px;top:74px;width:180px;text-align:center;font-size:11.5px;line-height:16px;color:var(--white)}

/* panorama */
.pano{grid-column:1 / 4;position:relative;overflow:hidden;background:linear-gradient(115deg,#B995E6,#A17BD3 35%,#8E5ED6 60%,#7C50BE)}
.pano .flowers-left{left:-40px;top:260px;width:620px;height:560px;background:radial-gradient(ellipse at 40% 60%,#e27ac0 0,#d45db0 30%,rgba(212,93,176,0) 68%)}
.pano .flowers-right{left:780px;top:40px;width:480px;height:760px;background:radial-gradient(ellipse at 60% 45%,#e58cc8 0,#d65fb1 32%,rgba(214,95,177,0) 70%)}
.pano .flowers-bottom{left:380px;top:520px;width:860px;height:300px;background:radial-gradient(ellipse at 55% 80%,#f2b0c4 0,#ee9aa9 35%,rgba(238,154,169,0) 72%)}
.pano .divider{top:0;width:1px;height:100%;background:rgba(255,255,255,.25)}
.pano .rowline{left:0;right:0;top:406px;height:1px;background:rgba(255,255,255,.25)}
.tag{position:absolute;transform:translateX(-50%);display:flex;flex-direction:column;align-items:center;gap:4px}
.tag span{display:block;background:rgba(244,236,252,.95);padding:2px 18px;font-size:16px;font-weight:500;color:var(--purple);white-space:nowrap}
.tag span.ar{font-family:"Cairo",sans-serif;background:var(--white);font-size:16px}
.pano .brand{font-size:13px}
</style>
</head>
<body>
<main class="grid">

  <section class="post p-tend">
    <div class="photo" role="img" aria-label="Groom in a grey suit holding a white bridal bouquet"></div>
    <div class="abs frame"></div>
    <p class="abs lead">If you tend to a</p>
    <p class="abs word script">flower</p>
    <p class="abs body">it will bloom<br>no matter how many<br>weeds surround it.</p>
  </section>

  <section class="post p-promo">
    <div class="brand"  style="left:20px;top:30px"><span class="dot"></span>Bloomvantra</div>
    <p class="abs title pinyon">Special<br>Promotion</p>
    <div class="abs arch-line"></div>
    <div class="photo" role="img" aria-label="Pink and white lisianthus in a white ceramic vase"></div>
    <p class="abs off"><b>15</b><span>%</span><i>OFF</i></p>
  </section>

  <section class="post p-orchid">
    <div class="photo" role="img" aria-label="Bride's hands with rings holding a pink orchid and rose bouquet"></div>
    <div class="abs corner" style="left:20px;top:20px;border-width:6px 0 0 6px"></div>
    <div class="abs corner" style="right:20px;top:20px;border-width:6px 6px 0 0"></div>
    <div class="abs corner" style="left:20px;bottom:20px;border-width:0 0 6px 6px"></div>
    <div class="abs corner" style="right:20px;bottom:20px;border-width:0 6px 6px 0"></div>
    <p class="abs lead">Orchids remind us to appreciate the</p>
    <p class="abs word script">fleeting moments</p>
    <p class="abs tail">of beauty in life</p>
  </section>

  <section class="post p-moment">
    <div class="abs card"></div>
    <div class="photo" role="img" aria-label="Preserved red roses in a glass dome beside dried pampas and books"></div>
    <p class="abs quote">Do not dwell in the past<br>Do not dream of the future<br>Concentrate the mind on the present</p>
    <p class="abs ghost brush">Moment</p>
    <p class="abs word brush">Moment</p>
  </section>

  <section class="post p-power">
    <div class="abs diag"></div>
    <div class="photo" role="img" aria-label="Red roses in a dark vase with a golden keepsake and a coffee cup"></div>
    <p class="abs text pinyon">The point of power is<br>always in the present<br>moment</p>
    <div class="brand"><span class="dot"></span>Bloomvantra</div>
  </section>

  <section class="post p-rose">
    <div class="photo" role="img" aria-label="Close-up of deep red roses"></div>
    <div class="abs card"></div>
    <div class="abs obj" role="img" aria-label="Golden keepsake clock with preserved flowers on a wooden crate"></div>
    <div class="abs frame"></div>
    <p class="abs small">A rose is not just a flower<br>it is a symbol of beauty,<br>love, and hope.</p>
    <p class="abs w beauty">beauty</p>
    <p class="abs w hope">hope</p>
    <p class="abs w love">love</p>
  </section>

  <section class="post p-each">
    <div class="abs arch"></div>
    <div class="photo" role="img" aria-label="Hand-tied bouquet of white roses, snapdragons and pink blooms"></div>
    <p class="abs text">Each <span class="s">moment</span><br>is a chance to make<br>a beautiful new<br><span class="s">memory</span><br>in your life</p>
  </section>

  <section class="post p-priceless">
    <div class="photo" role="img" aria-label="Bunch of red roses"></div>
    <div class="abs frame"></div>
    <div class="brand light"><span class="dot"></span>Bloomvantra</div>
    <p class="abs title script">Priceless Moments</p>
    <p class="abs sub">are the currency of happiness</p>
  </section>

  <section class="post p-collect">
    <div class="abs white"></div>
    <div class="abs band"></div>
    <div class="photo" role="img" aria-label="Purple hydrangea petals"></div>
    <div class="abs frame"></div>
    <p class="abs title script">Collect moments</p>
    <p class="abs sub">not things</p>
  </section>

  <section class="post p-remember">
    <div class="photo" role="img" aria-label="Magenta orchids in a bright room"></div>
    <div class="abs frame"></div>
    <p class="abs l1">We don’t remember days</p>
    <p class="abs l2 pinyon">we remember</p>
    <p class="abs l3 script">Moments</p>
  </section>

  <section class="post p-logo">
    <div class="brand"><span class="dot"></span>Bloomvantra</div>
  </section>

  <section class="post p-memories">
    <div class="abs card"></div>
    <div class="abs lav"></div>
    <div class="photo" role="img" aria-label="Bridal bouquet of pink roses and baby's breath on white fabric"></div>
    <div class="abs band"></div>
    <p class="abs word script">Memories</p>
    <div class="abs frame"></div>
    <p class="abs cap">Today’s Special Moments<br>are <b>tomorrow’s memories</b></p>
  </section>

  <section class="post p-journey">
    <div class="photo" role="img" aria-label="Florist's hands working with pliers at a workbench"></div>
    <div class="abs half"></div>
    <p class="abs text">A journey that started<br>in 2005</p>
  </section>

  <section class="post p-frozen">
    <div class="abs tear"></div>
    <div class="abs shade"></div>
    <div class="photo" role="img" aria-label="Black and white birthday cake with lit candles"></div>
    <p class="abs label">Moments Frozen in Time</p>
  </section>

  <section class="post p-quote">
    <div class="photo" role="img" aria-label="Black and white courtyard with climbing plants"></div>
    <div class="abs box"></div>
    <p class="abs mark m1">“</p>
    <p class="abs text">Our hearts stay connected to memories, No matter where life takes us, we don’t let go of the special moments and people shared in</p>
    <p class="abs mark m2">“</p>
  </section>

  <section class="pano">
    <div class="photo flowers-left" role="img" aria-label="Pink phalaenopsis orchids"></div>
    <div class="photo flowers-right" role="img" aria-label="Pink orchids and roses"></div>
    <div class="photo flowers-bottom" role="img" aria-label="Pink and peach roses with orchids"></div>
    <div class="abs divider" style="left:400px"></div>
    <div class="abs divider" style="left:800px"></div>
    <div class="abs rowline"></div>

    <div class="tag" style="left:195px;top:172px"><span>Preserved Flowers</span><span class="ar">الزهور المحفوظة</span></div>
    <div class="tag" style="left:535px;top:86px"><span>Gifts For</span><span class="ar">هدايا ل</span></div>
    <div class="tag" style="left:630px;top:204px"><span>Occassions</span><span class="ar">الزهور المحفوظة</span></div>
    <div class="tag" style="left:993px;top:138px"><span>Moments Frozen in Time</span><span class="ar">لحظات مجمدة في الوقت المناسب</span></div>
    <div class="brand" style="left:950px;top:360px"><span class="dot"></span>Bloomvantra</div>

    <div class="tag" style="left:121px;top:470px"><span>Bridal</span><span class="ar">زفافي</span></div>
    <div class="tag" style="left:270px;top:607px"><span>Roses</span><span class="ar">لورو</span></div>
    <div class="tag" style="left:600px;top:470px"><span>Passion Projects</span><span class="ar">مشاريع العاطفة</span></div>
    <div class="tag" style="left:980px;top:466px"><span>Year 2025</span><span class="ar">سنة 2025</span></div>
    <div class="brand" style="left:22px;top:722px"><span class="dot"></span>Bloomvantra</div>
  </section>

</main>
</body>
</html>
```